Product Description Graphic

We are designing a new product and need a better graphic to describe it.

We are not worried about names of the modules yet but want to be descriptive of capabilities. Right now "Present & CMA" should really be "Presentations & CMA".

I overall like the shape of the triangle and the arrow for Contacts but this is a very unsophisticated graphic done by a non-designer. Also need to better show that each block of capabilites will also have paywall capabilities.

Target Market(s)

Real Estate Brokerage Firms and Real Estate Agents

Industry/Entity Type

Real Estate

Colors

Designer to choose colors to be used in the design.

Requirements
Must have
• Sophisticated design. Paywall description embedded.

```html
<!DOCTYPE html>
<html lang="en">
<head>
<meta charset="utf-8">
<title>Product Capabilities Pyramid</title>
<link rel="stylesheet" href="https://fonts.googleapis.com/css2?family=Barlow+Condensed:wght@600&display=swap">
<style>
  :root {
    --ink: #000000;
    --paper: #ffffff;
    --blue: #0a6ee0;
    --pink: #ff4d7d;
    --teal: #55ddd0;
    --yellow: #ffc124;
    --orange: #ff733c;
  }
  html, body {
    margin: 0;
    padding: 0;
    width: 1200px;
    height: 800px;
    overflow: hidden;
    background: var(--ink);
  }
  .canvas {
    display: block;
    width: 1200px;
    height: 800px;
  }
  .frame { fill: var(--paper); }
  .module-email { fill: var(--blue); }
  .module-present { fill: var(--pink); }
  .module-contacts { fill: var(--teal); }
  .module-websites { fill: var(--yellow); }
  .module-mobile { fill: var(--orange); }
  .label {
    font-family: "Barlow Condensed", "Arial Narrow", sans-serif;
    font-weight: 600;
    font-size: 46px;
    fill: var(--ink);
    letter-spacing: 0.5px;
  }
  .callout-line { fill: none; stroke: var(--paper); stroke-width: 16; }
  .callout-dot { fill: none; stroke: var(--paper); stroke-width: 14; }
  .callout-text {
    font-family: "Barlow Condensed", "Arial Narrow", sans-serif;
    font-weight: 600;
    font-size: 96px;
    fill: var(--paper);
  }
  .icon { fill: var(--ink); }
  .icon-line { fill: none; stroke: var(--ink); }
</style>
</head>
<body>
<svg class="canvas" viewBox="0 0 2352 1568" xmlns="http://www.w3.org/2000/svg" role="img" aria-label="Product capabilities pyramid with paywall feature">
  <!-- paywall frame -->
  <g class="paywall-frame">
    <polygon class="frame" points="809,284 843,345 362,1065 298,1065"/>
    <polygon class="frame" points="955,530 1305,1065 1250,1065 925,582"/>
    <polygon class="frame" points="210,1216 737,1216 737,1258 184,1258"/>
    <polygon class="frame" points="751,1216 820,1216 820,1258 751,1258"/>
    <polygon class="frame" points="838,1216 1393,1216 1418,1258 838,1258"/>
  </g>

  <!-- modules -->
  <polygon class="module-email" points="851,358 941,514 587,1065 375,1065"/>
  <polygon class="module-present" points="917,592 1235,1065 988,1065 802,762"/>
  <polygon class="module-contacts" points="785,783 965,1065 820,1065 820,1202 751,1202 751,1065 607,1065"/>
  <polygon class="module-websites" points="290,1082 735,1082 735,1202 218,1202"/>
  <polygon class="module-mobile" points="836,1082 1314,1082 1385,1202 836,1202"/>

  <!-- email module -->
  <g class="email-icon" transform="translate(592,889) rotate(34)">
    <rect class="icon" x="-42" y="-30" width="84" height="60" rx="6"/>
    <polyline class="icon-line" points="-38,-24 0,6 38,-24" stroke-width="0" />
    <path d="M-34,-22 L0,4 L34,-22" fill="none" stroke="var(--blue)" stroke-width="6"/>
  </g>
  <g transform="translate(625,838) rotate(-56)">
    <text class="label" x="0" y="0">EMAIL NURTURE</text>
    <text class="label" x="0" y="46">PRINT &amp; SOCIALS</text>
  </g>

  <!-- presentations module -->
  <g class="presentation-icon" transform="translate(922,760) rotate(34)">
    <rect class="icon" x="-42" y="-32" width="84" height="54" rx="4"/>
    <rect x="-30" y="-20" width="40" height="28" fill="var(--pink)"/>
    <rect class="icon" x="-4" y="22" width="8" height="14"/>
    <rect class="icon" x="-20" y="34" width="40" height="6"/>
  </g>
  <g transform="translate(950,822) rotate(56)">
    <text class="label" x="0" y="0">PRESENTATIONS</text>
    <text class="label" x="0" y="46">&amp; CMA</text>
  </g>

  <!-- contacts module -->
  <g class="contact-icon">
    <circle class="icon" cx="790" cy="933" r="19"/>
    <path class="icon" d="M751,990 C751,960 771,950 790,950 C809,950 828,960 828,990 Z"/>
  </g>
  <text class="label" x="788" y="1042" text-anchor="middle">CONTACTS</text>

  <!-- websites module -->
  <g class="globe-icon">
    <circle class="icon-line" cx="432" cy="1145" r="36" stroke-width="8"/>
    <ellipse class="icon-line" cx="432" cy="1145" rx="14" ry="36" stroke-width="8"/>
    <line class="icon-line" x1="396" y1="1145" x2="468" y2="1145" stroke-width="8"/>
    <line class="icon-line" x1="402" y1="1127" x2="462" y2="1127" stroke-width="6"/>
    <line class="icon-line" x1="402" y1="1163" x2="462" y2="1163" stroke-width="6"/>
  </g>
  <text class="label" x="490" y="1138">WEBSITES</text>
  <text class="label" x="490" y="1182">&amp; LEADS</text>

  <!-- mobile module -->
  <g class="phone-icon">
    <rect class="icon" x="998" y="1102" width="52" height="86" rx="8"/>
    <rect x="1006" y="1112" width="36" height="54" fill="var(--orange)"/>
    <circle cx="1024" cy="1177" r="5" fill="var(--orange)"/>
  </g>
  <text class="label" x="1070" y="1160">MOBILE</text>

  <!-- paywall callout -->
  <path class="callout-line" d="M1043,672 H1318 V547 H1466"/>
  <circle class="callout-dot" cx="1497" cy="547" r="26"/>
  <text class="callout-text" x="1562" y="582">PAYWALL</text>
  <text class="callout-text" x="1562" y="678">FEATURE</text>
</svg>
</body>
</html>
```